Supplement Rebranding Bottle Design

READ WORD DOCUMENT ATTACHED.
We want to rebrand our current health supplements (see below). We do want it to be modern, vibrant and appealing. Very upscale and elegant as it targets primarily women.
Bottle size: see pictures for bottle size, along with sample bottles that we like; we’re open to any bottle similar to the ones attached.
Current bottles: So ideally, we’d keep the core color on each bottle with a new branding/bottle design. But we're open to your suggestion.

Target Market(s)

mostly women but shouldn't be overly feminine

Requirements
Must have
• see bottle sizes attached

```html
<!DOCTYPE html>
<html lang="en">
<head>
<meta charset="UTF-8">
<title>Liver Bloom – Supplement Label</title>
<link rel="stylesheet" href="https://fonts.googleapis.com/css2?family=Montserrat:wght@600&family=Archivo:wght@500&display=swap">
<style>
  :root {
    --page-bg: #e9e9ea;
    --label-deep: #3e0f63;
    --label-mid: #5a1d8a;
    --label-glow: #7a3aa8;
    --ink-light: #f7f2fb;
  }
  * { margin: 0; padding: 0; box-sizing: border-box; }
  html, body {
    width: 1200px;
    height: 1200px;
    overflow: hidden;
    background: var(--page-bg);
  }
  .canvas {
    width: 1200px;
    height: 1200px;
    display: flex;
    align-items: center;
    justify-content: center;
  }
  .label {
    width: 760px;
    height: 860px;
    border-radius: 18px;
    background: radial-gradient(ellipse at 50% 40%, var(--label-glow) 0%, var(--label-mid) 45%, var(--label-deep) 100%);
    display: flex;
    flex-direction: column;
    align-items: center;
    padding-top: 300px;
    color: var(--ink-light);
    text-align: center;
  }
  .product-name {
    font-family: "Montserrat", sans-serif;
    font-weight: 600;
    font-size: 66px;
    letter-spacing: 4px;
    line-height: 1;
  }
  .brand-mark {
    margin-top: 34px;
    width: 104px;
    height: 104px;
  }
  .tagline {
    margin-top: 42px;
    font-family: "Archivo", sans-serif;
    font-weight: 500;
    font-size: 24px;
    letter-spacing: 1.5px;
    line-height: 1.45;
  }
  .tagline sup { font-size: 13px; }
  .product-facts {
    margin-top: 70px;
    font-family: "Archivo", sans-serif;
    font-weight: 500;
    font-size: 21px;
    letter-spacing: 1px;
    line-height: 1.45;
  }
</style>
</head>
<body>
  <main class="canvas">
    <section class="label">
      <h1 class="product-name">LIVER BLOOM</h1>
      <svg class="brand-mark" viewBox="0 0 104 104" aria-hidden="true">
        <circle cx="52" cy="52" r="48" fill="none" stroke="#f7f2fb" stroke-width="2"/>
      </svg>
      <p class="tagline">REJUVENATING CLEANSE &amp;<br>DETOX FORMULA<sup>*</sup></p>
      <p class="product-facts">DIETARY SUPPLEMENT<br>120 VEGETABLE CAPSULES</p>
    </section>
  </main>
</body>
</html>
```